I have just launched a labour hire company and lookingfor a fresh vibrant website design

I need a landing page, a description of our services and capability, as well as an enquiries link, and register candidates link. My company is called Halvora recruitment and we supply labourers, excavator operators, and machine operators to the Civil and railway industries. I would like to stick to our logo theme and colours of Bright green, although I want a brighter green please than what I have. I have attached Images I like as well plaese. I do need a much bigger website eventually.

```html
<!DOCTYPE html>
<html lang="en">
<head>
<meta charset="utf-8">
<title>Halvora Recruitment</title>
<link rel="stylesheet" href="https://fonts.googleapis.com/css2?family=Michroma&family=Lato:wght@400;700&family=Oswald:wght@400&family=Jost:wght@400&family=Montserrat:wght@400;500&display=swap">
<style>
:root{
  --green:#3dbb4f;
  --green-deep:#2faa42;
  --black:#000;
  --white:#fff;
  --navy:#1e3c8c;
  --ink:#1a1a1a;
  --grey-bg:#f1f1f1;
  --hex-fill:#e4e4e4;
  --hex-inner:#d2d2d2;
  --muted:#8a8a8a;
}
*{box-sizing:border-box;margin:0;padding:0}
html,body{width:1200px;height:3653px;overflow:hidden}
body{position:relative;background:var(--white);font-family:"Lato",sans-serif;color:var(--ink)}
.abs{position:absolute}
.wide{font-family:"Michroma",sans-serif;text-transform:uppercase;white-space:nowrap}

/* header */
.topline{left:0;top:0;width:1200px;height:5px;background:var(--green)}
.brand{display:flex;align-items:center;gap:12px}
.brand-mark{width:30px;height:30px;background:var(--green)}
.brand-name{font-family:"Michroma",sans-serif;line-height:1;white-space:nowrap;text-transform:uppercase}
.brand-name b{display:block;font-weight:400;font-size:28px;letter-spacing:1px}
.brand-name span{display:block;font-size:11px;margin-top:6px;letter-spacing:.5px}
.site-brand{left:98px;top:24px}
.nav a{position:absolute;top:40px;font-family:"Michroma",sans-serif;font-size:13px;color:var(--ink);text-decoration:none;white-space:nowrap;text-transform:uppercase}
.nav .active::after{content:"";position:absolute;left:0;right:0;top:24px;height:3px;background:var(--green)}

/* hero */
.hero-photo{left:0;top:99px;width:1200px;height:574px;background:linear-gradient(100deg,#d8dcdf 0%,#c3c9cd 40%,#b8c4cc 60%,#dfe4e7 100%)}
.hero-box{left:102px;top:213px;width:489px;height:248px;background:var(--green);border-left:8px solid var(--green-deep);padding:22px 0 0 24px;color:var(--white)}
.hero-box .kicker{font-family:"Michroma",sans-serif;font-size:23px;text-transform:uppercase}
.hero-box h1{font-family:"Michroma",sans-serif;font-weight:400;font-size:38px;line-height:56px;text-transform:uppercase;margin-top:8px;white-space:nowrap;-webkit-text-stroke:1px var(--white)}
.btn-dark{display:inline-flex;align-items:center;justify-content:center;background:var(--black);color:var(--white);border-radius:26px;font-family:"Michroma",sans-serif;text-transform:uppercase;text-decoration:none}
.hero-box .btn-dark{position:absolute;left:23px;top:184px;width:200px;height:47px;font-size:13px}
.round-arrow{width:54px;height:54px;border-radius:50%;background:var(--green);display:flex;align-items:center;justify-content:center}

/* sections */
.section-title{left:0;width:1200px;text-align:center;font-family:"Michroma",sans-serif;text-transform:uppercase;font-size:32px}
.service-photo{top:866px;width:320px;height:227px}
.service-label{top:1118px;width:320px;text-align:center;font-family:"Michroma",sans-serif;font-size:15px;text-transform:uppercase}

.about-band{left:0;top:1317px;width:1200px;height:478px;background:var(--green)}
.about-bar{background:var(--green-deep)}
.about-photo{left:109px;top:1252px;width:447px;height:465px;background:linear-gradient(180deg,#8c8e95 0%,#c9a57c 45%,#7a5a32 100%)}
.about-title{left:610px;top:1352px;font-size:42px;color:var(--white)}
.about-text{left:610px;top:1425px;width:478px;font-size:14.5px;line-height:24.8px;color:var(--white)}
.about .btn-dark{position:absolute;left:607px;top:1646px;width:159px;height:46px;font-size:15px}

.step{width:200px;text-align:center}
.step-label{font-family:"Michroma",sans-serif;font-size:11.5px;line-height:18px;text-transform:uppercase;white-space:nowrap}

/* jobs */
.jobs-bg{left:0;top:2360px;width:1200px;height:860px;background:var(--grey-bg)}
.job-card{left:98px;width:1002px;height:151px;background:var(--white);border-radius:10px;box-shadow:0 2px 8px rgba(0,0,0,.12)}
.job-logo{position:absolute;left:18px;top:20px;width:104px;height:112px}
.job-logo text{font-family:"Lato",sans-serif;font-weight:700;font-size:15px;fill:var(--ink)}
.job-title{position:absolute;left:157px;top:26px;font-family:"Oswald",sans-serif;font-size:31px;color:var(--ink);white-space:nowrap}
.job-meta{position:absolute;top:86px;font-family:"Montserrat",sans-serif;font-size:14px;color:var(--muted);white-space:nowrap}
.job-pill{position:absolute;left:812px;top:35px;width:146px;height:40px;border:2px solid var(--green);border-radius:20px;color:#1d4fa0;font-family:"Montserrat",sans-serif;font-size:16px;display:flex;align-items:center;justify-content:center}
.job-age{position:absolute;left:840px;top:96px;font-family:"Montserrat",sans-serif;font-size:15px;color:#444}

/* footer */
.contact-item{display:flex;gap:14px;color:var(--white)}
.contact-icon{width:38px;height:38px;border:1px solid #777;border-radius:50%;flex:none;display:flex;align-items:center;justify-content:center}
.contact-item h4{font-family:"Michroma",sans-serif;font-weight:400;font-size:13px;text-transform:uppercase}
.contact-item p{font-family:"Lato",sans-serif;font-size:13px;line-height:22px;margin-top:4px}
.foot-nav{left:0;top:3505px;width:1200px;height:67px;background:var(--green)}
.foot-nav a{position:absolute;top:25px;font-family:"Michroma",sans-serif;font-size:14px;color:var(--ink);text-decoration:none;white-space:nowrap;text-transform:uppercase}
.copyright{left:0;top:3572px;width:1200px;height:81px;background:var(--black);color:var(--white);font-family:"Jost",sans-serif;font-size:18px;text-align:center;padding-top:26px}
</style>
</head>
<body>

<header>
  <div class="abs topline"></div>
  <div class="abs brand site-brand">
    <div class="brand-mark"></div>
    <div class="brand-name"><b>Halvora</b><span>Recruitment Pty Ltd</span></div>
  </div>
  <nav class="nav">
    <a class="active" href="#" style="left:438px">Home</a>
    <a href="#" style="left:537px">About Us</a>
    <a href="#" style="left:675px">Our Services</a>
    <a href="#" style="left:853px">Process</a>
    <a href="#" style="left:985px">Contact Us</a>
  </nav>
</header>

<section class="hero">
  <div class="abs hero-photo" role="img" aria-label="Site worker in a blue hard hat holding a clipboard and radio in a workshop"></div>
  <svg class="abs" style="left:0;top:540px" width="1200" height="140" viewBox="0 0 1200 140">
    <polygon points="0,16 600,133 1200,52 1200,140 0,140" fill="#fff"/>
    <polygon points="560,127 1200,34 1200,52 600,133" fill="#2faa42"/>
  </svg>
  <div class="abs hero-box">
    <div class="kicker">Welcome to</div>
    <h1>Halvora<br>Recruitment</h1>
    <a class="btn-dark" href="#">Get Started</a>
  </div>
  <div class="abs round-arrow" style="left:573px;top:646px">
    <svg width="20" height="34" viewBox="0 0 20 34"><path d="M10 2v28M3 22l7 9 7-9" stroke="#fff" stroke-width="3" fill="none"/></svg>
  </div>
</section>

<section class="services">
  <h2 class="abs section-title" style="top:782px;color:var(--navy);font-weight:400">Our Services</h2>
  <div class="abs service-photo" style="left:98px;background:linear-gradient(180deg,#c7c7c7,#e0592a 45%,#3a3a3a)" role="img" aria-label="Labourers in hi-vis work gear shovelling on a rail track"></div>
  <div class="abs service-photo" style="left:440px;background:linear-gradient(180deg,#cfe2ee,#d9733a 55%,#b9b9b0)" role="img" aria-label="Two orange excavators on a construction site"></div>
  <div class="abs service-photo" style="left:780px;background:linear-gradient(180deg,#b7b6b0,#c9a55a 45%,#a65d3a)" role="img" aria-label="Excavator loading a truck with red earth"></div>
  <div class="abs service-label" style="left:98px">Labourers</div>
  <div class="abs service-label" style="left:440px">Excavator Operators</div>
  <div class="abs service-label" style="left:780px">Machine Operators</div>
</section>

<section class="about">
  <div class="abs about-band"></div>
  <div class="abs about-bar" style="left:52px;top:1204px;width:30px;height:188px"></div>
  <div class="abs about-bar" style="left:109px;top:1204px;width:30px;height:48px"></div>
  <div class="abs about-bar" style="left:160px;top:1204px;width:187px;height:31px"></div>
  <div class="abs about-photo" role="img" aria-label="Yellow excavators at sunset under a cloudy sky"></div>
  <h2 class="abs wide about-title" style="font-weight:400">About Us</h2>
  <p class="abs about-text">Halvora Recruitment is a NSW labour hire agency specialising in the civil sector. With a strong track record of providing skilled and reliable workers to the civil and rail construction industry, we have established ourselves as a trusted partner for companies seeking efficient and cost-effective staffing solutions. Our team of experienced professionals is dedicated to meeting the specific needs of our clients, ensuring seamless project execution and successful outcomes.</p>
  <a class="btn-dark" href="#">See More</a>
</section>

<section class="process">
  <h2 class="abs section-title" style="top:1892px;font-weight:400">The Process</h2>

  <div class="abs step" style="left:91px;top:1992px">
    <svg width="200" height="204" viewBox="0 0 200 204" role="img" aria-label="Line icon of a factory"><polygon points="100,3 189,52 189,152 100,201 11,152 11,52" fill="#e4e4e4" stroke="#111" stroke-width="4"/><rect x="60" y="62" width="80" height="80" rx="6" fill="#d2d2d2"/></svg>
    <div class="step-label" style="margin-top:32px">Rigorous<br>selection process:</div>
  </div>
  <div class="abs step" style="left:296px;top:1992px">
    <svg width="200" height="204" viewBox="0 0 200 204" role="img" aria-label="Line icon of a facility on a gear"><polygon points="100,3 189,52 189,152 100,201 11,152 11,52" fill="#e4e4e4" stroke="#111" stroke-width="4"/><rect x="60" y="62" width="80" height="80" rx="6" fill="#d2d2d2"/></svg>
    <div class="step-label" style="margin-top:32px">Compliance<br>verification</div>
  </div>
  <div class="abs step" style="left:500px;top:1992px">
    <svg width="200" height="204" viewBox="0 0 200 204" role="img" aria-label="Line icon of a report with approve and reject marks"><polygon points="100,3 189,52 189,152 100,201 11,152 11,52" fill="#e4e4e4" stroke="#3dbb4f" stroke-width="4"/><rect x="60" y="62" width="80" height="80" rx="6" fill="#d2d2d2"/></svg>
    <div class="step-label" style="margin-top:32px">Reference checking</div>
  </div>
  <div class="abs step" style="left:704px;top:1992px">
    <svg width="200" height="204" viewBox="0 0 200 204" role="img" aria-label="Line icon of a cloud linked to three choices"><polygon points="100,3 189,52 189,152 100,201 11,152 11,52" fill="#e4e4e4" stroke="#111" stroke-width="4"/><rect x="60" y="62" width="80" height="80" rx="6" fill="#d2d2d2"/></svg>
    <div class="step-label" style="margin-top:32px">Skill assessment</div>
  </div>
  <div class="abs step" style="left:908px;top:1992px">
    <svg width="200" height="204" viewBox="0 0 200 204" role="img" aria-label="Line icon of an industrial plant"><polygon points="100,3 189,52 189,152 100,201 11,152 11,52" fill="#e4e4e4" stroke="#111" stroke-width="4"/><rect x="60" y="62" width="80" height="80" rx="6" fill="#d2d2d2"/></svg>
    <div class="step-label" style="margin-top:32px">Industry experience</div>
  </div>
</section>

<section class="jobs">
  <div class="abs jobs-bg"></div>
  <h2 class="abs section-title" style="top:2430px;font-weight:400">Job Search in Recruitment</h2>

  <article class="abs job-card" style="top:2514px">
    <svg class="job-logo" viewBox="0 0 104 112"><polygon points="52,2 100,29 100,83 52,110 4,83 4,29" fill="#fff" stroke="#e3e3e3" stroke-width="3"/><text x="52" y="61" text-anchor="middle">Corvane</text></svg>
    <div class="job-title">Duis aute irure dolor</div>
    <div class="job-meta" style="left:161px">Creative Agency</div>
    <div class="job-meta" style="left:380px">&#9679; Nemo enim ipsam</div>
    <div class="job-meta" style="left:592px;font-size:13px">$2500 - $3800</div>
    <div class="job-pill">Full time</div>
    <div class="job-age">8 Hours Ago</div>
  </article>
  <article class="abs job-card" style="top:2701px">
    <svg class="job-logo" viewBox="0 0 104 112"><polygon points="52,2 100,29 100,83 52,110 4,83 4,29" fill="#fff" stroke="#e3e3e3" stroke-width="3"/><text x="52" y="61" text-anchor="middle">Tillet</text></svg>
    <div class="job-title">Duis aute irure dolor</div>
    <div class="job-meta" style="left:161px">Creative Agency</div>
    <div class="job-meta" style="left:380px">&#9679; Nemo enim ipsam</div>
    <div class="job-meta" style="left:592px;font-size:13px">$2500 - $3800</div>
    <div class="job-pill">Full time</div>
    <div class="job-age">8 Hours Ago</div>
  </article>
  <article class="abs job-card" style="top:2887px">
    <svg class="job-logo" viewBox="0 0 104 112"><polygon points="52,2 100,29 100,83 52,110 4,83 4,29" fill="#fff" stroke="#e3e3e3" stroke-width="3"/><text x="52" y="61" text-anchor="middle">Bramlow</text></svg>
    <div class="job-title">Duis aute irure dolor</div>
    <div class="job-meta" style="left:161px">Creative Agency</div>
    <div class="job-meta" style="left:380px">&#9679; Nemo enim ipsam</div>
    <div class="job-meta" style="left:592px;font-size:13px">$2500 - $3800</div>
    <div class="job-pill">Full time</div>
    <div class="job-age">8 Hours Ago</div>
  </article>
</section>

<footer>
  <svg class="abs" style="left:0;top:3140px" width="1200" height="370" viewBox="0 0 1200 370">
    <polygon points="0,73 600,20 1200,115 1200,370 0,370" fill="#000"/>
    <polygon points="0,58 600,5 600,20 0,73" fill="#2faa42"/>
  </svg>
  <div class="abs round-arrow" style="left:573px;top:3145px">
    <svg width="20" height="34" viewBox="0 0 20 34"><path d="M10 32V4M3 12l7-9 7 9" stroke="#fff" stroke-width="3" fill="none"/></svg>
  </div>
  <div class="abs brand" style="left:438px;top:3250px;color:var(--white)">
    <div class="brand-mark"></div>
    <div class="brand-name"><b style="font-size:32px">Halvora</b><span style="font-size:13px">Recruitment Pty Ltd</span></div>
  </div>

  <div class="abs contact-item" style="left:123px;top:3413px">
    <div class="contact-icon"><svg width="16" height="12" viewBox="0 0 16 12"><rect x="1" y="1" width="14" height="10" fill="none" stroke="#fff" stroke-width="1.5"/><path d="M1 1l7 6 7-6" fill="none" stroke="#fff" stroke-width="1.5"/></svg></div>
    <div><h4>Email</h4><p>hello@halvorarecruitment.com.au</p></div>
  </div>
  <div class="abs contact-item" style="left:453px;top:3413px">
    <div class="contact-icon"><svg width="12" height="16" viewBox="0 0 12 16"><path d="M6 15s5-6 5-9.5a5 5 0 0 0-10 0C1 9 6 15 6 15z" fill="#fff"/><circle cx="6" cy="5.5" r="1.8" fill="#000"/></svg></div>
    <div><h4>Our Location</h4><p>19 Nemo enim ipsam voluptatem<br>quia voluptas sit</p></div>
  </div>
  <div class="abs contact-item" style="left:812px;top:3413px">
    <div class="contact-icon"><svg width="14" height="14" viewBox="0 0 14 14"><path d="M3 1l2 3-1.5 1.5a8 8 0 0 0 5 5L10 9l3 2-1.5 2.5C6 13 1 8 .8 2.5z" fill="#fff"/></svg></div>
    <div><h4>Phone Number</h4><p>1 300 555 017</p></div>
  </div>

  <nav class="abs foot-nav">
    <a href="#" style="left:269px">Home</a>
    <a href="#" style="left:368px">About Us</a>
    <a href="#" style="left:507px">Our Services</a>
    <a href="#" style="left:684px">Process</a>
    <a href="#" style="left:816px">Contact Us</a>
  </nav>
  <div class="abs copyright">Copyright © 2023 Northwell Studio - All Rights Reserved.</div>
</footer>

</body>
</html>
```